Quarlwick Builders Business Cards

I want to use the logo and make an unique business card that shows the textured Logo with brick and builings. I want to be able to stand out when I pass out business cards.

```html
<!DOCTYPE html>
<html lang="en">
<head>
<meta charset="utf-8">
<title>Quarlwick Builders Business Cards</title>
<link rel="stylesheet" href="https://fonts.googleapis.com/css2?family=Oswald:wght@500;600&family=Roboto:wght@500;700&family=Roboto+Condensed:wght@500&display=swap">
<style>
  :root {
    --stage: #2c2c2c;
    --card-dark: #171717;
    --concrete-light: #c9c8c3;
    --concrete-mid: #a3a29d;
    --concrete-dark: #7a7975;
    --brick-orange: #f15a24;
    --tag-navy: #1f2f4f;
    --white: #ffffff;
  }
  * { box-sizing: border-box; margin: 0; padding: 0; }
  html, body { width: 1200px; height: 1015px; overflow: hidden; background: var(--stage); }
  .stage { position: relative; width: 1200px; height: 1015px; }

  .card {
    position: absolute;
    width: 540px; height: 309px;
    overflow: hidden;
    box-shadow: 0 14px 30px rgba(0,0,0,.55);
    background: var(--card-dark);
  }
  .card--back { left: 70px; top: 110px; }
  .card--front { left: 590px; top: 560px; }

  .concrete {
    position: absolute;
    background:
      radial-gradient(ellipse at 30% 40%, rgba(255,255,255,.25), transparent 60%),
      radial-gradient(ellipse at 80% 70%, rgba(0,0,0,.2), transparent 60%),
      linear-gradient(135deg, var(--concrete-mid), var(--concrete-light) 55%, var(--concrete-dark));
  }
  .card--back .concrete { left: 0; top: 0; width: 100%; height: 175px; }
  .card--front .concrete { left: 44%; top: 0; width: 56%; height: 100%; }

  .brand {
    position: absolute;
    display: flex; flex-direction: column; align-items: center;
    text-align: center;
  }
  .brand__mark { display: flex; align-items: center; gap: 10px; white-space: nowrap; }
  .brand__square { width: 20px; height: 20px; background: var(--brick-orange); flex: none; }
  .brand__name {
    font-family: "Oswald", sans-serif; font-weight: 600;
    color: var(--brick-orange); text-transform: uppercase;
    letter-spacing: 1px; line-height: 1; white-space: nowrap;
  }
  .brand__services {
    margin-top: 10px;
    font-family: "Roboto Condensed", sans-serif; font-weight: 500;
    color: var(--tag-navy); font-size: 12px; white-space: nowrap;
  }
  .card--back .brand { left: 0; width: 100%; top: 82px; }
  .card--back .brand__name { font-size: 38px; }
  .card--front .brand { left: 44%; width: 56%; top: 118px; }
  .card--front .brand__mark { gap: 8px; }
  .card--front .brand__square { width: 16px; height: 16px; }
  .card--front .brand__name { font-size: 24px; }

  .contact { position: absolute; left: 34px; top: 70px; color: var(--white); }
  .contact__name {
    font-family: "Oswald", sans-serif; font-weight: 500;
    color: var(--brick-orange); font-size: 34px; text-transform: uppercase; line-height: 1;
  }
  .contact__role { font-family: "Roboto", sans-serif; font-weight: 700; font-size: 15px; margin-top: 4px; }
  .contact__list { list-style: none; margin-top: 16px; font-family: "Roboto", sans-serif; font-weight: 700; font-size: 14px; }
  .contact__list li { display: flex; align-items: center; gap: 8px; height: 21px; }
  .contact__list svg { width: 13px; height: 13px; flex: none; }
  .contact__address { margin-top: 14px; font-family: "Roboto", sans-serif; font-weight: 700; font-size: 14px; line-height: 1.35; }
</style>
</head>
<body>
<main class="stage">

  <section class="card card--back" aria-label="Card back">
    <div class="concrete" role="img" aria-label="Grey concrete wall texture"></div>
    <div class="brand">
      <div class="brand__mark">
        <span class="brand__square"></span>
        <span class="brand__name">Quarlwick Builders</span>
      </div>
      <p class="brand__services">Patios - Sidewalks - Retaining Walls - Foundations</p>
    </div>
  </section>

  <section class="card card--front" aria-label="Card front">
    <div class="concrete" role="img" aria-label="Grey concrete wall texture"></div>
    <div class="contact">
      <h1 class="contact__name">Dorian Vale</h1>
      <p class="contact__role">Managing Director</p>
      <ul class="contact__list">
        <li>
          <svg viewBox="0 0 24 24" fill="var(--brick-orange)"><path d="M6.6 10.8a15 15 0 0 0 6.6 6.6l2.2-2.2a1 1 0 0 1 1-.25 11.4 11.4 0 0 0 3.6.57 1 1 0 0 1 1 1V20a1 1 0 0 1-1 1A17 17 0 0 1 3 4a1 1 0 0 1 1-1h3.5a1 1 0 0 1 1 1c0 1.25.2 2.450 .57 3.57a1 1 0 0 1-.25 1z"/></svg>
          044-123 456 789
        </li>
        <li>
          <svg viewBox="0 0 24 24" fill="var(--brick-orange)"><path d="M2 5h20v14H2z M2 5l10 8 10-8" stroke="var(--card-dark)" stroke-width="1.5"/></svg>
          hello@quarlwick.com
        </li>
        <li>
          <svg viewBox="0 0 24 24" fill="none" stroke="var(--brick-orange)" stroke-width="2"><circle cx="12" cy="12" r="10"/><path d="M2 12h20M12 2c3 3 3 17 0 20M12 2c-3 3-3 17 0 20"/></svg>
          www.quarlwick.com
        </li>
      </ul>
      <p class="contact__address">421, Address line goes here,<br>45452,Country Name</p>
    </div>
    <div class="brand">
      <div class="brand__mark">
        <span class="brand__square"></span>
        <span class="brand__name">Quarlwick Builders</span>
      </div>
      <p class="brand__services">Patios - Sidewalks - Retaining Walls - Foundations</p>
    </div>
  </section>

</main>
</body>
</html>
```